Creative, Fun, Eye catching signage for new office - inspire and inform!

I am looking for a billboard sign, a smaller sign and a very small sign for parking spots. These will be located in our new office space. I have uploaded two logos, this way you can choose. I would love to see what it looks like with black behind the logo but am open to creative ideas. I would like the majority of the background to be black and/or white

1. Sign for over door – with five at the top like in the photo attached

The sign size is 2600mm (L) x 900mm (H)

Logo at the top then services to the right side
Social & Living Skills Programs
Support Workers
Respite/Supported Holidays
Exercise Physiology
Occupational Therapy
Speech Therapy
Psychology
Behavioural Therapy

I would like the design to tie in with the website and/or flyers/banners attached. Please also try and add 1800 527 930

2. Sign for glass roller door

745cm wide by 725cm high ( similar to what next door has without it saying parent )

Tallbrook Logo
Drop Off Zone

Smaller signs for parking spots
1000cm wide, 60cm high

Tallbrook logo Visitor Parking 24/7

I would like the design to be consistent across the three items so they work together but are not identical.

I have attached images showing what I am talking about in relation to the location of each sign.

Target Market(s)

Families, parents and people with disabilities

Industry/Entity Type

Disability and community service

Colors

Designer to choose colors to be used in the design.

Requirements
Must have
• White or black background - the logo and please use colours shown in the brochures and banners provided. Preferences are black white and yellow
Nice to have
• all of our services and website and/or 1800 527 930 on banner 1
Should not have
• I dont want it to be to busy please

```html
<!DOCTYPE html>
<html lang="en">
<head>
<meta charset="utf-8">
<title>Tallbrook Signage Set</title>
<link href="https://fonts.googleapis.com/css2?family=Montserrat:wght@400;500;600;700&display=swap" rel="stylesheet">
<style>
  :root {
    --backdrop: #d3d3d3;
    --paper: #ffffff;
    --sun: #fbd872;
    --sun-glow: #fdf0c2;
    --ink: #111111;
    --text: #333333;
    --tag: #2e2e2e;
  }
  * { margin: 0; padding: 0; box-sizing: border-box; }
  html, body { width: 1200px; height: 1200px; overflow: hidden; }
  body {
    background: var(--backdrop);
    font-family: "Montserrat", sans-serif;
    color: var(--ink);
    position: relative;
  }
  .sign {
    position: absolute;
    background: var(--paper);
    overflow: hidden;
    box-shadow: 0 10px 18px rgba(0,0,0,0.28);
  }
  .glow {
    position: absolute;
    border-radius: 50%;
    background: radial-gradient(circle, var(--sun-glow) 0%, rgba(253,240,194,0.5) 45%, rgba(255,255,255,0) 70%);
  }
  .shape { position: absolute; left: 0; top: 0; }
  .abs { position: absolute; }
  .brand {
    position: absolute;
    font-weight: 700;
    color: var(--ink);
    letter-spacing: 0.02em;
    text-transform: uppercase;
    white-space: nowrap;
  }
  .brand-dot { position: absolute; border-radius: 50%; background: var(--sun); }
  .tagline { position: absolute; font-weight: 400; line-height: 1.1; white-space: nowrap; }
  .tagline strong { font-weight: 700; }
  .call { position: absolute; font-weight: 700; text-transform: uppercase; white-space: nowrap; }
  .phone {
    position: absolute;
    background: var(--sun);
    border-radius: 10px;
    font-weight: 600;
    display: flex; align-items: center; justify-content: center;
    white-space: nowrap;
  }
  .services-tag {
    position: absolute;
    background: var(--tag);
    color: #fff;
    font-weight: 700;
    border-radius: 5px;
    display: flex; align-items: center; justify-content: center;
    text-transform: uppercase;
    white-space: nowrap;
  }
  .service-list { position: absolute; list-style: none; color: var(--text); font-weight: 500; }
  .service-list li { position: relative; white-space: nowrap; }
  .service-list li::before {
    content: ""; position: absolute; border-radius: 50%; background: var(--text);
  }

  /* Strip sign */
  .strip { left: 85px; top: 71px; width: 1030px; height: 62px; }
  .strip .brand { left: 21px; top: 21px; font-size: 15px; }
  .strip .brand-dot { left: 64px; top: 11px; width: 9px; height: 9px; }
  .strip .tagline { left: 123px; top: 20px; font-size: 11px; }
  .strip .call { left: 300px; top: 20px; width: 94px; text-align: center; font-size: 6px; }
  .strip .phone { left: 299px; top: 30px; width: 94px; height: 17px; font-size: 12.5px; border-radius: 4px; }
  .strip .services-tag { left: 451px; top: 8px; width: 88px; height: 12px; font-size: 8px; border-radius: 2px; }
  .strip .service-list { top: 28px; font-size: 7.5px; line-height: 13px; }
  .strip .service-list li::before { width: 2.5px; height: 2.5px; left: -11px; top: 5px; }

  /* Wide sign */
  .wide { left: 85px; top: 192px; width: 1030px; height: 356px; }
  .wide .brand { left: 116px; top: 63px; font-size: 32px; }
  .wide .brand-dot { left: 238px; top: 31px; width: 26px; height: 26px; }
  .wide .tagline { left: 94px; top: 118px; font-size: 35px; line-height: 40px; }
  .wide .call { left: 156px; top: 242px; width: 200px; text-align: center; font-size: 20px; }
  .wide .phone { left: 119px; top: 272px; width: 266px; height: 48px; font-size: 36px; }
  .wide .services-tag { left: 641px; top: 42px; width: 275px; height: 38px; font-size: 30px; }
  .wide .service-list { left: 697px; top: 94px; font-size: 19px; line-height: 29.8px; }
  .wide .service-list li::before { width: 6px; height: 6px; left: -20px; top: 12px; }

  /* Square sign */
  .square { left: 321px; top: 608px; width: 559px; height: 544px; }
  .square .brand { left: 0; width: 559px; text-align: center; top: 36px; font-size: 24px; }
  .square .brand-dot { left: 270px; top: 13px; width: 18px; height: 18px; }
  .square .tagline { left: 0; width: 559px; text-align: center; top: 76px; font-size: 25px; line-height: 29px; }
  .square .call { left: 0; width: 548px; text-align: center; top: 153px; font-size: 15px; }
  .square .phone { left: 199px; top: 174px; width: 190px; height: 35px; font-size: 26px; border-radius: 8px; }
  .square .services-tag { left: 170px; top: 367px; width: 216px; height: 30px; font-size: 23px; }
  .square .service-list { top: 421px; font-size: 15px; line-height: 23.3px; }
  .square .service-list li::before { width: 4.5px; height: 4.5px; left: -14px; top: 9px; }
</style>
</head>
<body>

  <!-- Strip sign -->
  <section class="sign strip" aria-label="Tallbrook parking strip sign">
    <div class="glow" style="left:100px;top:-120px;width:360px;height:300px;"></div>
    <svg class="shape" width="1030" height="62" viewBox="0 0 1030 62" aria-hidden="true">
      <path d="M440 0 H1030 V62 H440 C432 48 438 38 434 30 C430 20 436 10 440 0 Z" fill="var(--sun)"/>
      <path d="M428 2 C420 14 422 24 425 32 C428 42 418 48 432 60" fill="none" stroke="var(--ink)" stroke-width="4" stroke-linecap="round"/>
    </svg>
    <span class="brand-dot"></span>
    <span class="brand">Tallbrook</span>
    <p class="tagline">Investing in Your<br>Future With <strong>Tallbrook</strong></p>
    <p class="call">Call us now</p>
    <p class="phone">1800 527 930</p>
    <p class="services-tag">Our Services</p>
    <ul class="service-list" style="left:470px;"><li>Social &amp; Living Skills Programs</li><li>Support Workers</li></ul>
    <ul class="service-list" style="left:631px;"><li>Respite/Supported Holidays</li><li>Exercise Physiology</li></ul>
    <ul class="service-list" style="left:782px;"><li>Occupational Therapy</li><li>Speech Therapy</li></ul>
    <ul class="service-list" style="left:917px;"><li>Psychology</li><li>Behavioural Therapy</li></ul>
  </section>

  <!-- Wide sign -->
  <section class="sign wide" aria-label="Tallbrook over-door sign">
    <div class="glow" style="left:20px;top:80px;width:500px;height:420px;"></div>
    <svg class="shape" width="1030" height="356" viewBox="0 0 1030 356" aria-hidden="true">
      <path d="M640 0 H1030 V356 H655 C620 335 595 310 594 284 C608 270 620 262 617 240 C612 200 596 150 590 100 C588 60 605 25 640 0 Z" fill="var(--sun)"/>
      <path d="M587 12 C565 40 555 70 560 100 C568 150 595 190 598 228 C600 252 585 262 567 278 C575 305 595 330 620 350" fill="none" stroke="var(--ink)" stroke-width="9" stroke-linecap="round" stroke-linejoin="round"/>
    </svg>
    <span class="brand-dot"></span>
    <span class="brand">Tallbrook</span>
    <p class="tagline">Investing in Your<br>Future With <strong>Tallbrook</strong></p>
    <p class="call">Call us now</p>
    <p class="phone">1800 527 930</p>
    <p class="services-tag">Our Services</p>
    <ul class="service-list">
      <li>Social &amp; Living Skills Programs</li>
      <li>Support Workers</li>
      <li>Respite/Supported Holidays</li>
      <li>Exercise Physiology</li>
      <li>Occupational Therapy</li>
      <li>Speech Therapy</li>
      <li>Psychology</li>
      <li>Behavioural Therapy</li>
    </ul>
  </section>

  <!-- Square sign -->
  <section class="sign square" aria-label="Tallbrook roller door sign">
    <div class="glow" style="left:20px;top:20px;width:520px;height:380px;"></div>
    <svg class="shape" width="559" height="544" viewBox="0 0 559 544" aria-hidden="true">
      <path d="M0 375 C30 330 70 300 105 293 L125 318 C200 332 320 292 420 285 C500 282 545 330 559 375 V544 H0 Z" fill="var(--sun)"/>
      <path d="M5 330 C40 285 80 258 110 245 L132 266 C200 290 320 250 420 236 C470 230 505 255 534 282" fill="none" stroke="var(--ink)" stroke-width="13" stroke-linecap="round" stroke-linejoin="round"/>
    </svg>
    <span class="brand-dot"></span>
    <span class="brand">Tallbrook</span>
    <p class="tagline">Investing in Your<br>Future With <strong>Tallbrook</strong></p>
    <p class="call">Call us now</p>
    <p class="phone">1800 527 930</p>
    <p class="services-tag">Our Services</p>
    <ul class="service-list" style="left:55px;">
      <li>Social &amp; Living Skills Programs</li>
      <li>Support Workers</li>
      <li>Respite/Supported Holidays</li>
      <li>Exercise Physiology</li>
    </ul>
    <ul class="service-list" style="left:340px;">
      <li>Occupational Therapy</li>
      <li>Speech Therapy</li>
      <li>Psychology</li>
      <li>Behavioural Therapy</li>
    </ul>
  </section>

</body>
</html>
```